TVRB web site redesign

Meridale Linkworks Provisioning service (TVRB) is a diverse technology company specialising in design and installation of fibre optics, network convergence and building services, for commercial clients in Australia, we required a new design of our website to attract new clients, generate sales leads, and provide information about our services to the market. The site and should have a new technology look and feel and be designed in word press. our branding colour is blue.

Target Market(s)

New developments, Construction organisations, Commercial end users, IT managers, Consultants.

Industry/Entity Type

It Company

Number of Pages Required

5+ page

Font styles to use
Sans Serif

Colors
0292cd
3176b5

Requirements
Must have
• key pages.
• Home page with some sizzle, automated pictures running through, I like the look of this competitor website http://www.lumacrest.com.au/ good clean menus and easy to navigate.
• Services page our key services are Fibre optics, Security, Building services,Electrical. I would like the same page layout (Design) for all our services, with a find out more link on each page, manly picture driven with text around our key messaging.
• About us page with space for company profile and directors pictures, bio and contact information.
• Certifications / Accreditations page with have over 20 certifications on different products from suppliers, and a number of licences from governing bodies.
• Current and past projects page with case studies and customer outcomes
• Contact us page with options around what services they require more information on, please keep in mind the site is around generating sales Leeds and being seen as an industry expert.
Nice to have
• RSS feeds, Linked in link, to be placed within the design, Consistent TVRB branding,Same colour blue as our logo Document library for education information, white papers, presentations etc,
• a new technology look and feel, mobile friendly.
Should not have
• boring layout, move away from our cuurent website http://www.tvrbgroup.com.au/
• no e eCommerce store required.

```html
<!DOCTYPE html>
<html lang="en">
<head>
<meta charset="utf-8">
<title>TVRB — Technology Services</title>
<link rel="stylesheet" href="https://fonts.googleapis.com/css2?family=Open+Sans:wght@400;600&family=Ubuntu:wght@400;500&display=swap">
<style>
:root{
  --brand:#0a7fbe;
  --brand-dark:#056ea8;
  --brand-deep:#03639a;
  --accent:#3176b5;
  --sky:#0292cd;
  --ink:#444;
  --muted:#777;
  --band:#f4f4f4;
  --white:#fff;
  --yellow:#f6c21c;
}
*{box-sizing:border-box;margin:0;padding:0}
html,body{width:684px;height:1200px;overflow:hidden;background:#fff}
body{position:relative;font-family:"Open Sans",Arial,sans-serif;color:var(--ink)}
.abs{position:absolute}

/* header */
.site-header{left:0;top:0;width:684px;height:75px;background:var(--brand)}
.brand{left:34px;top:10px;color:var(--white);font-family:"Ubuntu",sans-serif;font-weight:500}
.brand-name{font-size:38px;line-height:40px;letter-spacing:1px}
.brand-sub{font-size:6.4px;letter-spacing:.1px;text-transform:uppercase;margin-top:2px;width:135px;white-space:nowrap;overflow:hidden}
.call{right:34px;top:13px;color:var(--white);font-size:8px}
.call span{font-size:10px}
.main-nav{left:262px;top:36px;display:flex;height:39px}
.main-nav a{color:var(--white);font-size:8.2px;text-decoration:none;padding:0 11.5px;line-height:39px}
.main-nav a.active{background:var(--brand-deep);padding:0 14px}
.dropdown{left:262px;top:75px;width:107px;background:var(--brand-deep);list-style:none}
.dropdown li{font-size:6.4px;color:var(--white);padding:0 13px;height:23.2px;line-height:23.2px;border-bottom:1px solid rgba(255,255,255,.08)}

/* hero */
.hero{left:0;top:75px;width:684px;height:351px;background:linear-gradient(90deg,#3d5a78 0%,#b9c6d2 30%,#e3e9ef 55%,#f2f5f8 100%)}
.hero-copy{left:398px;top:176px;font-family:"Ubuntu",sans-serif;color:#333;font-size:12.5px;line-height:26.5px}
.hero-copy b{font-weight:500;color:var(--accent);font-size:18px}
.hero-copy .l1 b{color:var(--sky)}
.dots{left:633px;top:399px;display:flex;gap:3px}
.dots i{width:5px;height:5px;border-radius:50%;background:#cfd6dc}
.dots i:first-child{background:var(--sky)}

/* welcome */
.welcome{left:0;top:447px;width:684px;text-align:center}
.welcome h1{font-family:"Ubuntu",sans-serif;font-weight:400;font-size:17px;color:#444}
.welcome p{width:560px;margin:12px auto 0;font-size:8.2px;line-height:12.6px;color:#555}
.btn{display:inline-block;color:var(--white);font-size:7.2px;height:17px;line-height:17px;padding:0 13px;margin:12px 3px 0}
.btn-dark{background:var(--accent);width:66px}
.btn-sky{background:var(--sky)}

/* service cards */
.card{top:590px;width:183px;text-align:center}
.card-media{height:100px}
.card h3{font-family:"Ubuntu",sans-serif;font-weight:400;font-size:9.6px;color:#333;margin-top:10px;line-height:12.8px}
.card h3.hl{color:var(--accent);font-weight:500}
.card p{font-size:6px;line-height:8.8px;color:var(--muted);margin:7px 8px 0}
.overlay-btn{left:50px;top:41px;width:78px;height:19px;border:1px solid rgba(255,255,255,.8);color:var(--white);font-size:8.2px;line-height:17px;text-align:center}

/* product feature */
.feature{left:0;top:827px;width:684px;height:183px;background:var(--band)}
.device{left:52px;top:798px;width:72px;height:198px;border-radius:7px;background:linear-gradient(#2d2a2b,#141213);border:3px solid #2ba0dc;box-shadow:0 4px 6px rgba(0,0,0,.25)}
.feature h2{left:158px;top:848px;font-family:"Ubuntu",sans-serif;font-weight:400;font-size:16px;color:#444}
.feature-text{left:160px;top:880px;width:465px;font-size:7.2px;line-height:9.9px;color:#555}
.feature-text p+p{margin-top:10px}
.more{left:568px;top:986px;width:55px;height:15px;background:var(--sky);color:var(--white);font-size:7.2px;text-align:center;line-height:15px}

/* footer */
.site-footer{left:0;top:1010px;width:684px;height:157px;background:var(--brand)}
.col{top:1041px;color:var(--white)}
.col h4{font-size:7px;font-weight:600;letter-spacing:.5px;margin-bottom:6px}
.col p,.col li{font-size:6px;line-height:9.8px}
.col ul{list-style:none}
.col-links li{line-height:12.6px;font-weight:600}
.divider{top:1040px;width:1px;height:104px;background:rgba(255,255,255,.12)}
.group{font-family:"Ubuntu",sans-serif;font-size:17px;line-height:18px;letter-spacing:1px;margin-bottom:3px}
.contact-line{display:flex;align-items:center;gap:7px;margin-top:3px}
.field{width:121px;height:16px;background:#2294cf;font-size:5.4px;line-height:16px;padding-left:6px;margin-top:6px}
.send{width:47px;height:13px;background:var(--yellow);color:var(--brand-deep);font-size:6.2px;text-align:center;line-height:13px;margin:10px 0 0 74px}
.bottom-bar{left:0;top:1167px;width:684px;height:33px;background:var(--brand-deep)}
.social{left:34px;top:1181px;display:flex;gap:8px}
.social i{width:6px;height:6px;border-radius:50%;background:var(--white)}
.copy{right:34px;top:1179px;color:var(--white);font-size:6.4px}
</style>
</head>
<body>

<header class="abs site-header"></header>
<div class="abs brand">
  <div class="brand-name">TVRB</div>
  <div class="brand-sub">Meridale Linkworks Provisioning service</div>
</div>
<div class="abs call">Call Us : <span>1300 415 962</span></div>
<nav class="abs main-nav">
  <a class="active">Home</a><a>Services</a><a>About us</a><a>Certifications</a><a>Current / Past Projects</a><a>Contacts</a>
</nav>

<section class="abs hero" role="img" aria-label="Technician in a suit working on a laptop beside a fibre network rack"></section>
<ul class="abs dropdown">
  <li>Fibre optics</li><li>Security</li><li>Building services</li><li>Electrical</li>
</ul>
<div class="abs hero-copy">
  <div class="l1"><b>TVRB</b> has an</div>
  <div style="padding-left:33px"><b>Exceptional Team</b></div>
  <div>of very <b>Experienced</b> and</div>
  <div><b>well - qualified management</b></div>
  <div>and <b>Tradespersons</b></div>
</div>
<div class="abs dots"><i></i><i></i><i></i><i></i></div>

<section class="abs welcome">
  <h1>Welcome To our Site</h1>
  <p>TVRB is diversified technology company 100% Australian owned and operated, we provide Communication, Electrical, Security &amp; ICT services for residential and commercial customers. With over 100 years of combined industry knowledge we pride ourselves on innovated solutions that utilises technology advancements which delivers on our customer's expectations.</p>
  <span class="btn btn-dark">Read More</span><span class="btn btn-sky">View Products</span>
</section>

<article class="abs card" style="left:35px">
  <div class="card-media" style="position:relative;background:linear-gradient(#2d97cc,#1b86bf)" role="img" aria-label="Security cameras under a blue tint">
    <div class="abs overlay-btn">Read More</div>
  </div>
  <h3 class="hl">Commercial Security Systems</h3>
  <p>TVRB offers a wide range of IP commercial security solutions, from a small standalone system to our fully integrated enterprise systems.</p>
</article>
<article class="abs card" style="left:250px">
  <div class="card-media" style="background:linear-gradient(135deg,#1d4fa8,#3a8fd8 50%,#c9b640)" role="img" aria-label="Glass globe resting on patch panels and fibre cables"></div>
  <h3>Data &amp; Fibre Installations</h3>
  <p>TVRB has highly trained and proficient engineers, technicians and project managers to ensure that we achieve a high quality Data or Fibre Network, on time and within Budget.</p>
</article>
<article class="abs card" style="left:466px">
  <div class="card-media" style="background:radial-gradient(circle at 45% 45%,#3a8ee8,#0b2f7a 70%,#061a4a)" role="img" aria-label="Glowing world network connections"></div>
  <h3>Information Communication &amp;<br>Technology</h3>
  <p>Information Communication Technology (ICT) is often used in many different applications and services. At TVRB the key area of our ICT capabilities is around</p>
</article>

<section class="abs feature"></section>
<div class="abs device" role="img" aria-label="Black access card reader product"></div>
<h2 class="abs feature" style="background:none;height:auto;width:auto;left:158px;top:848px;font-family:'Ubuntu',sans-serif;font-weight:400;font-size:16px;color:#444">Reader</h2>
<div class="abs feature-text">
  <p>Phasellus viverra vel arcu ac aliquam. Quisque rutrum, ante iaculis rutrum interdum, nulla diam dictum orci, in commodo odio sapien ut nibh. Aliquam erat volutpat. Nunc nisl ligula, ultricies quis posuere vel, egestas quis massa. Fusce quis mauris cursus, hendrerit ligula feugiat, rutrum eros. Vestibulum vel elementum mauris. Integer risus ipsum, efficitur non viverra sed, dapibus non nulla.</p>
  <p>Nunc fermentum diam id felis tempor consectetur. Cras et nisi ullamcorper, cursus dui ut, egestas tortor. Praesent semper ante a massa pulvinar porttitor. Nulla pharetra, ligula in fringilla semper, turpis risus volutpat dui, at pellentesque eros leo pretium eros. Maecenas facilisis orci vel nibh cursus dapibus.</p>
</div>
<div class="abs more">More</div>

<footer class="abs site-footer"></footer>
<div class="abs col" style="left:34px;width:130px">
  <h4>ABOUT US</h4>
  <div class="group">TVRB GROUP</div>
  <p>Dr. Lorne Vasquell received his training in Gastroenterology and Liver Disease from the State University of</p>
  <svg width="6" height="5" style="margin:3px 0 0 116px" viewBox="0 0 6 5"><path d="M0 2.5h5M3 .5l2 2-2 2" stroke="#fff" fill="none" stroke-width=".8"/></svg>
  <div class="contact-line" style="margin-top:6px"><svg width="5" height="7" viewBox="0 0 5 7"><rect x=".5" y=".5" width="4" height="6" rx=".8" fill="none" stroke="#fff" stroke-width=".8"/></svg><p>Telephone 1300 415 962</p></div>
  <div class="contact-line"><svg width="6" height="5" viewBox="0 0 6 5"><rect x=".4" y=".4" width="5.2" height="4.2" fill="none" stroke="#fff" stroke-width=".7"/><path d="M.4.4l2.6 2.2L5.6.4" stroke="#fff" fill="none" stroke-width=".7"/></svg><p>hello@tvrbgroup.com.au</p></div>
  <div class="contact-line"><svg width="6" height="6" viewBox="0 0 6 6"><rect x="0" y="2" width="6" height="4" fill="#fff"/><rect x="1.2" y="0" width="3.6" height="2.4" fill="none" stroke="#fff" stroke-width=".7"/></svg><p>Fax: (02) 9471 3380</p></div>
</div>
<div class="abs divider" style="left:187px"></div>
<div class="abs col col-links" style="left:224px">
  <h4>USEFUL LINKS</h4>
  <ul><li>Home</li><li>Services</li><li>About us</li><li>Certifications</li><li>Current / Past Projects</li><li>Contacts</li></ul>
</div>
<div class="abs divider" style="left:319px"></div>
<div class="abs col" style="left:351px;width:120px">
  <h4>GET IN TOUCH</h4>
  <p>Lorem ipsum dolor sit amet, consectetur adipiscing elit. Proin at accumsan ligula.</p>
  <div style="display:flex;gap:12px;margin-top:8px">
    <svg width="4" height="6" viewBox="0 0 4 6"><path d="M2 6C.5 3.8 0 3 0 2a2 2 0 0 1 4 0c0 1-.5 1.8-2 4z" fill="#8fc8e8"/></svg>
    <p>Suite 4B, 12-14 Corvin Parade<br>Hollis Ridge NSW 2158<br>PO Box 2284 NSW 1771</p>
  </div>
</div>
<div class="abs divider" style="left:495px"></div>
<div class="abs col" style="left:527px;width:125px">
  <h4>CONTACT</h4>
  <p>Conecus iure posae volor remped modis</p>
  <div class="field" style="margin-top:8px">Name</div>
  <div class="field">Enter your email address</div>
  <div class="send">CONTACT</div>
</div>

<div class="abs bottom-bar"></div>
<div class="abs social" aria-label="Social links"><i></i><i></i><i></i><i></i></div>
<div class="abs copy">© 2015 tvrbgroup. All rights reserved.</div>

</body>
</html>
```